Opening new doors for every person - Solvane-Ridge

Please note that whoever will win this project , a 1on1 Powerpoint design project will separately be launched and will be offered to the winning designer.

---------
This letterhead is to provide proposals, as well as manuals for my clients.

I am looking for the letter, power point design and business card that inspires people when they see it, that they feel that design has been done with love and passion. Something that is professional, simple and yet creative, Business like, yet spiritual. That inspires growth!

This part of the branding for my company, therefore the business card as well as the power point design that will come after as 1on1 project should have the same team and feeling.

Solvane ridge, The company will be providing Coaching services (one-one or groups) to corporations, teams and individuals, partnering with them to achieve their goals/vision, by helping them to remove the self-imposed limiting beliefs, helping them to get them out of their own way, helping them to raise their level of consciousness and self-awareness.

The vision is: Bring conscious leadership to the workplace and to individuals for the wellbeing of humanity.

I know that somewhere out there will resonate with this, and will be inspired to provide the best design :) thank you very much!!!!!

MPORTANT:
- To use Free Fonts - let me know where I can download them
- Editable formats please for the double sized business card

LOGO is attached in pdf. If needed other file type please let me know

Thank you thank you in advance for your time and inspiration!! Sending good vibes for a great design out there

Must Have:
- Please keep on mind that the cards - power point will have the same feeling - Corporate branding
- that is not to heavy to look at it, that is simple and beautiful and inspiring
- Looking to have Calibri or Calibri light font

imple, yet inspirational - Professional, yet playful - business like, yet spiritual

I am looking for something different that the "standard" designs out there.

For example, the Logo of the company in the back side with a quote and the front side something simple, yet inspiring. that has the contact info as well as the social media details LinkedIn - Facebook - tweeter - website

Open for suggestions and inspiration :)

Thank you!

• - Please keep on mind that the cards - power point will have the same feeling
• - Corporate branding
• - that is not to heavy to look at it, that is simple and beautiful and inspiring
• - Looking to have Calibri or Calibri light font
• - Corporate colours as the logo

```html
<!DOCTYPE html>
<html lang="en">
<head>
<meta charset="utf-8">
<title>Solvane-Ridge — Business Card</title>
<link rel="stylesheet" href="https://fonts.googleapis.com/css2?family=Source+Sans+3:wght@400;600;700&display=swap">
<style>
  :root {
    --stage: #000000;
    --paper: #ffffff;
    --brand-blue: #1c4a8b;
    --brand-gold: #fbbd18;
    --back-gold: #fdbf1c;
    --back-gold-deep: #f6b413;
    --ink: #1a1a1a;
  }
  * { margin: 0; padding: 0; box-sizing: border-box; }
  html, body {
    width: 1200px; height: 900px; overflow: hidden;
    background: var(--stage);
  }
  .canvas {
    position: relative; width: 1200px; height: 900px;
    font-family: "Source Sans 3", "Segoe UI", sans-serif;
  }

  .card {
    position: absolute; top: 275px; width: 477px; height: 293px;
    overflow: hidden;
  }
  .card--front {
    left: 116px; background: var(--paper);
    border-radius: 0 48px 0 48px;
    color: var(--ink);
  }
  .card--back {
    left: 622px;
    border-radius: 48px 0 48px 0;
  }
  .back-field {
    position: absolute; inset: 0;
    background: radial-gradient(ellipse at 45% 55%, var(--back-gold-deep) 0%, var(--back-gold) 60%);
  }

  /* front: brand block */
  .brand-dot {
    position: absolute; left: 40px; top: 66px; width: 86px; height: 86px;
    border-radius: 50%; background: var(--brand-gold);
  }
  .brand-rule {
    position: absolute; left: 141px; top: 61px; width: 2px; height: 101px;
    background: var(--brand-blue);
  }
  .brand-name {
    position: absolute; left: 151px; top: 96px;
    font-weight: 600; font-size: 20px; line-height: 24px;
    color: var(--brand-gold); white-space: nowrap;
  }

  /* front: person & contact */
  .person, .address, .contact-list {
    position: absolute; right: 19px; text-align: right;
  }
  .person { top: 34px; }
  .person__name {
    font-weight: 700; font-size: 20px; line-height: 24px; color: var(--brand-blue);
  }
  .person__role { font-size: 13.5px; line-height: 17px; }
  .address { top: 157px; font-size: 13.5px; line-height: 17.5px; font-style: normal; }
  .contact-list { top: 217px; list-style: none; right: 20px; }
  .contact-list li {
    display: flex; align-items: center; justify-content: flex-end; gap: 7px;
    font-size: 13.5px; line-height: 17.5px;
  }
  .contact-list svg { width: 11px; height: 11px; fill: var(--brand-blue); }

  /* back */
  .back-name {
    position: absolute; left: 87px; top: 203px;
    font-weight: 600; font-size: 30px; line-height: 36px;
    color: var(--paper); white-space: nowrap;
  }
</style>
</head>
<body>
<main class="canvas">
  <section class="card card--front">
    <div class="brand-dot"></div>
    <div class="brand-rule"></div>
    <div class="brand-name">Solvane-Ridge</div>

    <div class="person">
      <div class="person__name">Marcus Ellery</div>
      <div class="person__role">Managing Director</div>
    </div>

    <address class="address">
      4820, Larkfield Avenue<br>Northvale, 560218
    </address>

    <ul class="contact-list">
      <li>041-555 208 316
        <svg viewBox="0 0 24 24" aria-hidden="true"><path d="M6.6 10.8a15.1 15.1 0 0 0 6.6 6.6l2.2-2.2c.3-.3.7-.4 1-.2 1.1.4 2.3.6 3.6.6.6 0 1 .4 1 1V20c0 .6-.4 1-1 1A17 17 0 0 1 3 4c0-.6.4-1 1-1h3.5c.6 0 1 .4 1 1 0 1.3.2 2.5.6 3.6.1.3 0 .7-.2 1z"/></svg>
      </li>
      <li>hello@solvane.com
        <svg viewBox="0 0 24 24" aria-hidden="true"><path d="M2 5h20v14H2z M3.5 6.5 12 12.5l8.5-6z" fill-rule="evenodd"/></svg>
      </li>
      <li>www.solvaneridge.com
        <svg viewBox="0 0 24 24" aria-hidden="true"><path d="M10.6 13.4a1 1 0 0 1 0-1.4l3.5-3.5a1 1 0 1 1 1.4 1.4L12 13.4a1 1 0 0 1-1.4 0zm-1.4 5.3a3.5 3.5 0 0 1-5-5l2.8-2.8 1.4 1.4-2.8 2.8a1.5 1.5 0 0 0 2.1 2.1l2.8-2.8 1.4 1.4zm8.4-5.3-1.4-1.4 2.8-2.8a1.5 1.5 0 0 0-2.1-2.1l-2.8 2.8-1.4-1.4 2.8-2.8a3.5 3.5 0 0 1 5 5z"/></svg>
      </li>
    </ul>
  </section>

  <section class="card card--back">
    <div class="back-field" role="img" aria-label="Large faint brand emblem in deeper gold tones across the card back"></div>
    <div class="back-name">Solvane-Ridge</div>
  </section>
</main>
</body>
</html>
```